Lantrn & Ladle Festival poster,rack card, business card

We need phase 1 of the 1st annual Lantern & Ladle Festival to be held June 12 &13 2015. Location and etc to be given upon completion. We need a Poster design for store windows, a rack card for rack display, and a business size card to hand out to prospective exhibitors and attendees. The festival will focus on Food trucks and food vendors, along with multiple bands to play throughout the event . Additional work will be asked for after the phase one is complete, and we have more info such as sponsors and bands.

Attn all designers...... I opologize for the extreme delay on the project. I had an incendent that landed me in the hospital on sept 7, and I will not be released until next week ,at which time we will come to a decision. Thanks for your patience. Milo

```html
<!DOCTYPE html>
<html lang="en">
<head>
<meta charset="utf-8">
<title>Lantern &amp; Ladle Festival — Poster</title>
<link rel="stylesheet" href="https://fonts.googleapis.com/css2?family=Passion+One:wght@400;700&family=Oswald:wght@500;600&family=Montserrat:wght@700&display=swap">
<style>
  :root {
    --bg-deep: #1e1230;
    --bg-mid: #3d2656;
    --bg-glow: #5a3a78;
    --lime: #b8e639;
    --lime-shadow: #5f8a12;
    --ribbon: #e8502e;
    --ribbon-dark: #a8321b;
    --cream: #f3ecdf;
    --gold: #f2a531;
    --gold-light: #ffd36a;
    --teal: #35c3c0;
    --magenta: #d0467f;
  }
  * { margin: 0; padding: 0; box-sizing: border-box; }
  html, body { width: 849px; height: 1200px; overflow: hidden; background: var(--bg-deep); }
  .poster {
    position: relative;
    width: 849px;
    height: 1200px;
    overflow: hidden;
    background:
      radial-gradient(ellipse 60% 45% at 50% 45%, var(--bg-glow) 0%, transparent 70%),
      radial-gradient(ellipse 90% 80% at 50% 50%, var(--bg-mid) 0%, var(--bg-deep) 100%);
  }
  .guitar-art {
    position: absolute;
    left: -40px;
    top: 40px;
    width: 190px;
    height: 1100px;
    border-radius: 0 90px 120px 0;
    background: linear-gradient(180deg, rgba(53,195,192,0.55) 0%, rgba(208,70,127,0.45) 55%, rgba(53,195,192,0.5) 100%);
  }
  .fork-art {
    position: absolute;
    left: 655px;
    top: 560px;
    width: 110px;
    height: 600px;
    border-radius: 50px 50px 30px 30px;
    background: linear-gradient(180deg, var(--gold-light) 0%, var(--gold) 60%, #c87a1c 100%);
    opacity: 0.9;
  }
  .notes-art {
    position: absolute;
    left: 205px;
    top: 230px;
    width: 440px;
    height: 230px;
    border-radius: 50%;
    background: radial-gradient(ellipse at center, rgba(255,211,106,0.18) 0%, transparent 70%);
  }
  .headline {
    position: absolute;
    left: 0;
    right: 0;
    top: 360px;
    text-align: center;
  }
  .headline__edition {
    font-family: "Oswald", sans-serif;
    font-weight: 600;
    font-size: 40px;
    letter-spacing: 4px;
    color: var(--cream);
    line-height: 1;
  }
  .headline__title {
    margin-top: 14px;
    font-family: "Passion One", sans-serif;
    font-weight: 700;
    color: var(--lime);
    text-transform: uppercase;
    text-shadow: 0 6px 0 var(--lime-shadow), 0 12px 18px rgba(0,0,0,0.45);
  }
  .headline__title .line-one { display: block; font-size: 128px; line-height: 0.92; letter-spacing: 2px; }
  .headline__title .line-two { display: block; font-size: 110px; line-height: 0.95; }
  .headline__title .small-word { font-size: 62px; vertical-align: 22px; margin-right: 8px; }
  .ribbon {
    position: relative;
    display: inline-block;
    margin-top: 22px;
    padding: 8px 34px 6px;
    background: var(--ribbon);
    color: var(--cream);
    font-family: "Passion One", sans-serif;
    font-size: 48px;
    letter-spacing: 3px;
    line-height: 1;
    transform: rotate(-3deg);
    box-shadow: 0 8px 14px rgba(0,0,0,0.35);
  }
  .ribbon::before, .ribbon::after {
    content: "";
    position: absolute;
    top: 10px;
    width: 24px;
    height: 100%;
    background: var(--ribbon-dark);
    z-index: -1;
  }
  .ribbon::before { left: -16px; }
  .ribbon::after { right: -16px; }
  .event-date {
    position: absolute;
    left: 78px;
    top: 1010px;
    font-family: "Montserrat", sans-serif;
    font-weight: 700;
    font-size: 38px;
    letter-spacing: 6px;
    color: var(--cream);
    line-height: 1.3;
  }
</style>
</head>
<body>
  <main class="poster">
    <div class="guitar-art" role="img" aria-label="Illustration of an electric guitar in teal and pink along the left edge"></div>
    <div class="notes-art" role="img" aria-label="Scattered golden music notes around the headline"></div>
    <div class="fork-art" role="img" aria-label="Illustration of a golden fork standing upright"></div>

    <header class="headline">
      <p class="headline__edition">1ST ANNUAL</p>
      <h1 class="headline__title">
        <span class="line-one">Lantern</span>
        <span class="line-two"><span class="small-word">&amp;</span>Ladle</span>
      </h1>
      <span class="ribbon">FESTIVAL</span>
    </header>

    <p class="event-date">JUNE 12-13<br>2015</p>
  </main>
</body>
</html>
```